Business Card and Stationary for an Executive and Life Coaching company
Harbor Kindle
Simple
Lina Brook, KLV, DRT
Executive Life Coach
2873 Wexbury Ln. Suite 615
Naples, FL 34782
Lina@HarborKindle.example
www.HarborKindle.example
I've included logo for KLV, and instructions on where and how to place it.
I'd like the design to be simple and uncluttered, while enticing people to want to be part of the movement and program because it is fun, smart, and provides tangible and positive results.
I'd like simple but unique fonts.
rise to new heights (on top)
(1 letter logo may go in the middle)
Growth Coach to Bright Leaders and Founders. (bottom of card)

```html
<!DOCTYPE html>
<html lang="en">
<head>
<meta charset="utf-8">
<title>Harbor Kindle Stationery</title>
<link href="https://fonts.googleapis.com/css2?family=Open+Sans:wght@400;600;700&display=swap" rel="stylesheet">
<style>
  :root {
    --bg: #e4e4e4;
    --paper: #ffffff;
    --green: #5d6d4f;
    --gold: #a8895a;
    --grey: #555555;
    --text: #6a6a6a;
    --cream: #e8e2d4;
  }
  * { margin: 0; padding: 0; box-sizing: border-box; }
  html, body { width: 1200px; height: 1011px; overflow: hidden; }
  body { background: var(--bg); font-family: "Open Sans", Arial, sans-serif; color: var(--text); position: relative; }

  .sheet { position: absolute; background: var(--paper); box-shadow: 0 2px 6px rgba(0,0,0,.18); overflow: hidden; }

  .brand { display: flex; align-items: center; gap: 8px; }
  .brand-mark { width: 22px; height: 22px; background: var(--gold); flex: none; }
  .brand-name { font-weight: 700; color: var(--green); font-size: 24px; letter-spacing: -.3px; white-space: nowrap; }

  .address { font-size: 9px; line-height: 1.5; color: var(--text); white-space: nowrap; }

  .swoosh { position: absolute; left: 0; bottom: 0; width: 100%; display: block; }
  .web { position: absolute; left: 18px; bottom: 8px; font-size: 9px; color: #fff; letter-spacing: .3px; white-space: nowrap; }

  /* letterhead */
  .letterhead { left: 60px; top: 80px; width: 540px; height: 699px; }
  .letterhead .brand { position: absolute; left: 160px; top: 64px; }
  .letterhead .address { position: absolute; right: 40px; top: 36px; }

  /* envelope */
  .envelope { left: 650px; top: 80px; width: 490px; height: 230px; }
  .envelope .band { position: absolute; right: 0; top: 0; width: 260px; height: 130px; }
  .envelope .brand { position: absolute; left: 28px; top: 42px; }
  .envelope .brand-name { font-size: 20px; }
  .envelope .address { position: absolute; left: 28px; top: 84px; }

  /* card back */
  .card-back { left: 650px; top: 350px; width: 350px; height: 200px; background: var(--green); border-radius: 8px; }
  .card-back .tagline { position: absolute; top: 22px; width: 100%; text-align: center; color: #fff; font-size: 14px; letter-spacing: .5px; }
  .card-back .strap { position: absolute; bottom: 16px; left: 18px; color: var(--cream); font-size: 8px; white-space: nowrap; }

  /* card front */
  .card-front { left: 650px; top: 590px; width: 350px; height: 200px; }
  .card-front .brand { position: absolute; right: 20px; top: 18px; }
  .card-front .brand-name { font-size: 18px; }
  .card-front .person { position: absolute; right: 20px; top: 58px; text-align: right; }
  .person-name { font-size: 11px; font-weight: 600; color: var(--grey); }
  .person-title { font-size: 9px; color: var(--text); }
  .contact { margin-top: 8px; font-size: 8px; line-height: 1.5; color: var(--text); }
</style>
</head>
<body>

<section class="sheet letterhead">
  <div class="brand"><span class="brand-mark"></span><span class="brand-name">Harbor Kindle</span></div>
  <div class="address">
    2873 Wexbury Ln. Suite 615<br>Naples, FL 34782<br>T 239 555 0142<br>F 239 555 0198<br>Lina@HarborKindle.example
  </div>
  <svg class="swoosh" viewBox="0 0 540 140" preserveAspectRatio="none" height="140">
    <path d="M0,22 C180,12 360,60 540,108 L540,140 L0,140 Z" fill="var(--grey)"/>
    <path d="M0,42 C180,36 360,82 540,124 L540,140 L0,140 Z" fill="var(--paper)"/>
    <path d="M0,48 C180,42 360,86 540,128 L540,140 L0,140 Z" fill="var(--green)"/>
    <path d="M0,72 C200,70 380,112 540,140 L0,140 Z" fill="var(--gold)"/>
  </svg>
  <span class="web">www.HarborKindle.example</span>
</section>

<section class="sheet envelope">
  <svg class="band" viewBox="0 0 260 130" preserveAspectRatio="none">
    <path d="M0,0 L260,0 L260,130 C200,80 120,30 0,18 Z" fill="var(--green)"/>
  </svg>
  <div class="brand"><span class="brand-mark"></span><span class="brand-name">Harbor Kindle</span></div>
  <div class="address">2873 Wexbury Ln. Suite 615<br>Naples, FL 34782</div>
  <svg class="swoosh" viewBox="0 0 490 70" preserveAspectRatio="none" height="70">
    <path d="M0,8 C140,4 300,30 490,70 L0,70 Z" fill="var(--grey)"/>
    <path d="M0,22 C140,18 300,42 490,70 L0,70 Z" fill="var(--paper)"/>
    <path d="M0,26 C140,22 300,46 490,70 L0,70 Z" fill="var(--green)"/>
    <path d="M0,42 C160,40 320,58 420,70 L0,70 Z" fill="var(--gold)"/>
  </svg>
  <span class="web">www.HarborKindle.example</span>
</section>

<section class="sheet card-back">
  <p class="tagline">rise to new heights</p>
  <p class="strap">Growth Coach to Bright Leaders and Founders.</p>
</section>

<section class="sheet card-front">
  <div class="brand"><span class="brand-mark"></span><span class="brand-name">Harbor Kindle</span></div>
  <div class="person">
    <p class="person-name">Lina Brook, KLV, DRT</p>
    <p class="person-title">Executive Life Coach</p>
    <p class="contact">T 239 555 0142<br>C 239 555 0175<br>Lina@HarborKindle.example</p>
  </div>
  <svg class="swoosh" viewBox="0 0 350 60" preserveAspectRatio="none" height="60">
    <path d="M0,6 C100,2 220,26 350,58 L350,60 L0,60 Z" fill="var(--grey)"/>
    <path d="M0,18 C100,15 220,36 350,60 L0,60 Z" fill="var(--paper)"/>
    <path d="M0,22 C100,19 220,40 350,60 L0,60 Z" fill="var(--green)"/>
    <path d="M0,36 C110,34 220,50 300,60 L0,60 Z" fill="var(--gold)"/>
  </svg>
  <span class="web">www.HarborKindle.example</span>
</section>

</body>
</html>
```